New Business Card Design Project

Use the flyer uploaded and website www.brightoakbuilders.com for inspiration.
List Our Services on Backside of business cards
Martin Hollis
Harborline Renovations Inc.
Licensed General Contractors
858-471-9063

Contact Information for Business Card

Use the flyer uploaded and website www.brightoakbuilders.com for inspiration. List Our Services on Backside of business cards Martin Hollis Harborline Renovations Inc. Licensed General Contractors 858-471-9063

```html
<!DOCTYPE html>
<html lang="en">
<head>
<meta charset="utf-8">
<title>Harborline Renovations – Business Card</title>
<link href="https://fonts.googleapis.com/css2?family=Roboto:wght@400;700&family=Roboto+Condensed:wght@400;700&display=swap" rel="stylesheet">
<style>
  :root {
    --stage: #e6e6e6;
    --card-dark: #3b3b3d;
    --card-light: #ffffff;
    --ink: #1f1f1f;
    --ink-soft: #6b6b6b;
    --on-dark: #ffffff;
    --art: #4a4a4c;
    --divider: #9a9a9a;
  }
  * { box-sizing: border-box; margin: 0; padding: 0; }
  html, body { width: 1200px; height: 874px; overflow: hidden; }
  body {
    background: var(--stage);
    font-family: "Roboto", Arial, sans-serif;
    color: var(--ink);
    position: relative;
  }
  .card {
    position: absolute;
    left: 250px;
    width: 700px;
    height: 400px;
    border-radius: 22px;
    overflow: hidden;
    box-shadow: 0 6px 18px rgba(0,0,0,.18);
  }
  /* Back side */
  .card--back { top: 22px; background: var(--card-dark); color: var(--on-dark); }
  .services {
    position: absolute;
    left: 44px; top: 40px;
    font-family: "Roboto Condensed", Arial, sans-serif;
    font-size: 17px;
    line-height: 1.45;
  }
  .services strong { font-weight: 700; }
  .services .sep { padding: 0 4px; }
  .skyline-art {
    position: absolute;
    right: 0; bottom: 0;
    width: 520px; height: 280px;
    background: linear-gradient(160deg, var(--card-dark) 0%, var(--art) 100%);
    border-top-left-radius: 8px;
  }
  /* Front side */
  .card--front { top: 452px; background: var(--card-light); }
  .brand {
    position: absolute;
    left: 40px; top: 150px;
    width: 280px;
    display: flex; align-items: center; gap: 12px;
  }
  .brand__mark {
    width: 18px; height: 18px;
    background: var(--ink);
    flex: none;
  }
  .brand__name {
    font-size: 25px;
    font-weight: 400;
    letter-spacing: .5px;
    line-height: 1.15;
    color: var(--ink);
  }
  .divider {
    position: absolute;
    left: 348px; top: 110px;
    width: 1px; height: 170px;
    background: linear-gradient(var(--divider), transparent);
  }
  .person { position: absolute; left: 378px; top: 110px; }
  .person__name {
    font-family: "Roboto Condensed", Arial, sans-serif;
    font-weight: 700;
    font-size: 32px;
    letter-spacing: .5px;
    text-transform: uppercase;
  }
  .person__role { font-size: 15px; color: var(--ink-soft); margin-top: 2px; }
  .contacts { list-style: none; margin-top: 26px; font-size: 17px; }
  .contacts li { display: flex; align-items: center; gap: 12px; margin-bottom: 6px; }
  .contacts svg { width: 14px; height: 14px; fill: var(--ink); flex: none; }
  .company-line {
    position: absolute;
    left: 0; right: 0; bottom: 36px;
    text-align: center;
    font-family: "Roboto Condensed", Arial, sans-serif;
    font-size: 18px;
    color: var(--ink-soft);
  }
  .company-line .sep { padding: 0 10px; }
</style>
</head>
<body>

<section class="card card--back">
  <div class="services">
    <p><strong>Remodel :</strong> Kitchen &amp; Bath <span class="sep">|</span> <strong>Painting :</strong> Interior &amp; Exterior</p>
    <p><strong>Flooring :</strong> Carpet, Vinyl, Wood <span class="sep">|</span> Window &amp; Door Replacement</p>
    <p><strong>Plumbing :</strong> Repairs &amp; Upgrades <span class="sep">|</span> Energy- Efficient Upgrades</p>
    <p>Deck &amp; Pation Construction <span class="sep">|</span> Water &amp; Mold Damage</p>
    <p>Garage Renovation</p>
  </div>
  <div class="skyline-art" role="img" aria-label="Line illustration of a modern house roofline with a palm tree"></div>
</section>

<section class="card card--front">
  <div class="brand">
    <span class="brand__mark"></span>
    <span class="brand__name">Harborline Renovations</span>
  </div>
  <div class="divider"></div>
  <div class="person">
    <h1 class="person__name">Martin Hollis</h1>
    <p class="person__role">President</p>
    <ul class="contacts">
      <li>
        <svg viewBox="0 0 24 24"><path d="M6.6 10.8a15.1 15.1 0 0 0 6.6 6.6l2.2-2.2c.3-.3.7-.4 1-.2 1.1.4 2.3.6 3.6.6.6 0 1 .4 1 1V20c0 .6-.4 1-1 1A17 17 0 0 1 3 4c0-.6.4-1 1-1h3.5c.6 0 1 .4 1 1 0 1.3.2 2.5.6 3.6.1.3 0 .7-.2 1z"/></svg>
        858-471-9063
      </li>
      <li>
        <svg viewBox="0 0 24 24"><path d="M2 5h20v14H2zm2 2v.5l8 5 8-5V7l-8 5z"/></svg>
        info@brightoakbuilders.com
      </li>
      <li>
        <svg viewBox="0 0 24 24"><circle cx="12" cy="12" r="10"/></svg>
        www.brightoakbuilders.com
      </li>
    </ul>
  </div>
  <p class="company-line">Harborline Renovations Inc.<span class="sep">|</span>Licensed General Contractors</p>
</section>

</body>
</html>
```